Business Stationery - Business Cards - Letterheads, Compliment Slips

We need a new set of artwork designed for our client, they are a Construction Company, that also sell Kitchens, bathrooms and appliances.
They are an up and comping company that focus on quality and bespoke build. For them it is all about the quality of what they install, build or design. They have recently been awarded sole distributorship of a German kitchen brand Annelore Kuchen.
We need to present a quick job to them and provide some proofs for their new Artwork which encompasses all the elements of the company
The company name is the Halvorn Group and we need to design a logo also.
Any Questions please let me know asap

Target Market(s)
Upmarket clients, or small Development companies.
Industry/Entity Type
Business
Look and feel

```html
<!DOCTYPE html>
<html lang="en">
<head>
<meta charset="utf-8">
<title>Halvorn Group – Stationery Set</title>
<link rel="stylesheet" href="https://fonts.googleapis.com/css2?family=PT+Sans:wght@400;700&display=swap">
<style>
  :root {
    --brand-blue: #0d5bb5;
    --brand-blue-deep: #0a4f9e;
    --brand-blue-glow: #2a7fe0;
    --brand-green: #3a9a3c;
    --paper: #ffffff;
    --ink: #333333;
    --rule: #c9c9c9;
    --page-bg: #ffffff;
    --shadow: 0 2px 8px rgba(0,0,0,0.22);
  }
  * { box-sizing: border-box; margin: 0; padding: 0; }
  html, body { width: 1200px; height: 1200px; overflow: hidden; background: var(--page-bg); }
  body { position: relative; font-family: "PT Sans", sans-serif; color: var(--ink); }

  .wordmark { display: inline-flex; align-items: center; gap: 8px; font-family: "PT Sans", sans-serif; font-weight: 700; white-space: nowrap; }
  .wordmark__square { display: inline-block; background: currentColor; }

  /* Presentation folder */
  .folder {
    position: absolute; left: 107px; top: 69px; width: 460px; height: 594px;
    background: radial-gradient(circle at 50% 42%, var(--brand-blue-glow) 0%, #1a6bd0 30%, var(--brand-blue) 60%, var(--brand-blue-deep) 100%);
    box-shadow: var(--shadow); overflow: hidden;
  }
  .folder__emblem {
    position: absolute; left: 130px; top: 165px; width: 200px; height: 200px; border-radius: 50%;
    background: rgba(10,70,150,0.28);
  }
  .folder .wordmark { position: absolute; right: 24px; bottom: 27px; color: #fff; font-size: 23px; }
  .folder .wordmark__square { width: 16px; height: 16px; }

  /* Letterhead */
  .letterhead {
    position: absolute; left: 633px; top: 69px; width: 460px; height: 594px;
    background: var(--paper); box-shadow: var(--shadow); overflow: hidden;
  }
  .letterhead__edge { position: absolute; left: 0; top: 0; width: 16px; height: 100%; background: var(--brand-blue); }
  .letterhead .wordmark { position: absolute; left: 80px; top: 56px; color: var(--brand-blue); font-size: 19px; gap: 6px; }
  .letterhead .wordmark__square { width: 13px; height: 13px; }
  .contact-tab {
    position: absolute; right: 0; top: 44px; width: 174px; height: 54px; padding: 6px 10px 0 30px;
    background: var(--brand-blue); color: #fff; font-size: 7.5px; line-height: 10px;
    box-shadow: -2px 3px 6px rgba(0,0,0,0.25);
  }
  .contact-tab__row { display: flex; align-items: center; gap: 5px; }
  .contact-tab__row svg { width: 7px; height: 7px; fill: #fff; }
  .contact-tab__web { margin-top: 3px; padding-top: 2px; text-align: center; border-top: 1px solid rgba(255,255,255,0.5); margin-left: -20px; }
  .letter__rule { position: absolute; left: 93px; top: 160px; width: 1px; height: 222px; background: var(--rule); }
  .letter__salutation { position: absolute; left: 113px; top: 142px; font-size: 9px; }
  .letter__body { position: absolute; left: 147px; top: 164px; width: 262px; font-size: 8.4px; line-height: 11.2px; text-align: justify; }
  .letter__body p { text-indent: 32px; margin-bottom: 11px; }
  .letter__signature { position: absolute; left: 330px; top: 384px; width: 90px; height: 26px; background: linear-gradient(90deg, rgba(40,40,40,0.15), rgba(40,40,40,0.05)); }
  .letterhead__emblem { position: absolute; right: -70px; bottom: -60px; width: 220px; height: 220px; border-radius: 50%; background: rgba(13,91,181,0.1); }

  /* Primary logo */
  .primary-logo { position: absolute; left: 110px; top: 920px; color: var(--brand-blue); font-size: 56px; gap: 18px; }
  .primary-logo .wordmark__square { width: 44px; height: 44px; }

  /* Business cards */
  .card { position: absolute; width: 340px; height: 196px; box-shadow: var(--shadow); overflow: hidden; }
  .card--front { left: 640px; top: 740px; background: var(--paper); }
  .card--back { left: 770px; top: 900px; background: radial-gradient(circle at 30% 30%, #2a7fe0 0%, var(--brand-blue) 55%, var(--brand-blue-deep) 100%); }
  .card--front .wordmark { position: absolute; left: 20px; top: 24px; color: var(--brand-blue); font-size: 17px; gap: 6px; }
  .card--front .wordmark__square { width: 11px; height: 11px; }
  .card__tagline { position: absolute; left: 150px; top: 30px; font-size: 6.5px; color: #777; }
  .card__emblem { position: absolute; right: 16px; top: 10px; width: 64px; height: 64px; border-radius: 50%; background: rgba(13,91,181,0.14); }
  .card__web { position: absolute; right: 18px; top: 86px; font-size: 8px; color: var(--brand-green); }
  .card__rule { position: absolute; left: 20px; right: 18px; top: 98px; height: 1px; background: var(--brand-green); opacity: 0.6; }
  .card__name { position: absolute; left: 22px; top: 114px; font-size: 10px; color: var(--brand-blue); }
  .card__role { position: absolute; left: 22px; top: 127px; font-size: 7px; color: var(--brand-green); }
  .card__contacts { position: absolute; left: 22px; top: 142px; font-size: 7px; line-height: 11px; color: var(--brand-blue); }
  .card__contacts div { display: flex; align-items: center; gap: 5px; }
  .card__contacts svg { width: 6px; height: 6px; fill: var(--brand-green); }
  .card--back .card__emblem { right: auto; left: 40px; top: 26px; width: 96px; height: 96px; background: rgba(255,255,255,0.12); }
  .card--back .wordmark { position: absolute; right: 110px; bottom: 20px; color: #fff; font-size: 15px; gap: 6px; }
  .card--back .wordmark__square { width: 10px; height: 10px; }
  .card--back .card__tagline { left: auto; right: 16px; top: auto; bottom: 24px; color: #dce8f7; }
</style>
</head>
<body>
  <svg width="0" height="0" style="position:absolute" aria-hidden="true">
    <symbol id="icon-phone" viewBox="0 0 10 10"><rect x="2.5" y="0" width="5" height="10" rx="1"/></symbol>
    <symbol id="icon-fax" viewBox="0 0 10 10"><rect x="0" y="3" width="10" height="6" rx="1"/><rect x="2" y="0" width="6" height="3"/></symbol>
    <symbol id="icon-mail" viewBox="0 0 10 10"><rect x="0" y="2" width="10" height="7"/></symbol>
  </svg>

  <section class="folder" aria-label="Presentation folder">
    <div class="folder__emblem"></div>
    <div class="wordmark"><span class="wordmark__square"></span>Halvorn Group</div>
  </section>

  <section class="letterhead" aria-label="Letterhead">
    <div class="letterhead__edge"></div>
    <div class="wordmark"><span class="wordmark__square"></span>Halvorn Group</div>
    <div class="contact-tab">
      <div class="contact-tab__row"><svg><use href="#icon-phone"/></svg>555-014-2281</div>
      <div class="contact-tab__row"><svg><use href="#icon-fax"/></svg>555-017-6340</div>
      <div class="contact-tab__row"><svg><use href="#icon-mail"/></svg>e.marwood@halvorngroup.co</div>
      <div class="contact-tab__web">www.halvorngroup.co</div>
    </div>
    <div class="letter__rule"></div>
    <p class="letter__salutation">Dear&nbsp; Noor Lindqvist</p>
    <div class="letter__body">
      <p>Quaestione igitur per multiplices dilatata fortunas cum ambigerentur quaedam, non nulla levius actitata constaret, post multorum clades Apollinares ambo pater et filius in exilium acti cum ad locum Crateras nomine .</p>
      <p>Vbi curarum abiectis ponderibus aliis tamquam nodum et codicem difficillimum Caesarem convellere nisu valido cogitabat, eique deliberanti cum proximis clandestinis conloquiis et nocturnis qua vi, quibusve commentis id fieret, antequam effundendis rebus perti.</p>
      <p>Vbi curarum abiectis ponderibus aliis tamquam nodum et codicem difficillimum Caesarem convellere nisu valido cogitabat, eique deliberanti cum proximis clandestinis conloquiis et nocturnis qua vi, quibusve commentis id fieret, antequam effundendis rebus perti.</p>
    </div>
    <div class="letter__signature" role="img" aria-label="Handwritten signature"></div>
    <div class="letterhead__emblem"></div>
  </section>

  <div class="wordmark primary-logo"><span class="wordmark__square"></span>Halvorn Group</div>

  <section class="card card--front" aria-label="Business card front">
    <div class="wordmark"><span class="wordmark__square"></span>Halvorn Group</div>
    <span class="card__tagline">| Brenmoor Capital Ltd</span>
    <div class="card__emblem"></div>
    <div class="card__web">www.halvorngroup.co</div>
    <div class="card__rule"></div>
    <div class="card__name">Ellis Marwood</div>
    <div class="card__role">Owner</div>
    <div class="card__contacts">
      <div><svg><use href="#icon-phone"/></svg>555-014-2281</div>
      <div><svg><use href="#icon-fax"/></svg>555-017-6340</div>
      <div><svg><use href="#icon-mail"/></svg>e.marwood@halvorngroup.co</div>
    </div>
  </section>

  <section class="card card--back" aria-label="Business card back">
    <div class="card__emblem"></div>
    <div class="wordmark"><span class="wordmark__square"></span>Halvorn Group</div>
    <span class="card__tagline">| Brenmoor Capital Ltd</span>
  </section>
</body>
</html>
```